Marcus Delwyn-Hart Finance

Need a personal website advertising Equipment Finance,Business Finance,Commercial Finance, Construction Finance, Bridging Finance. Similar websites are www.qorvimark.com.au / www.talsbrio.com.au / www.zpk7.com.au /wwwlemberwick.com.au

Target Market(s)

Business People

Industry/Entity Type

Business

Number of Pages Required

3 page

Font styles to use
Serif
Sans Serif

Requirements
Must have
• All i want is a simple corporate looking website advertising Equipment Finance, Commercial Finance, Construction Finance, Business Finance, Bridging Finance,

```html
<!DOCTYPE html>
<html lang="en">
<head>
<meta charset="utf-8">
<title>Marcus Delwyn-Hart Finance</title>
<link rel="stylesheet" href="https://fonts.googleapis.com/css2?family=Lato:wght@300;400;700;900&family=Open+Sans:wght@400;600;700&display=swap">
<style>
:root{
  --blue:#1c9ad6;
  --blue-dark:#1588c2;
  --ink:#2b2b2b;
  --text:#3a3a3a;
  --muted:#777;
  --dark:#2f2a2a;
  --grey-band:#b9b9b9;
  --grey-soft:#efefef;
  --white:#fff;
  --red:#d8262b;
}
*{box-sizing:border-box;margin:0;padding:0}
html,body{width:1200px;height:3913px;overflow:hidden;background:var(--white)}
body{font-family:"Open Sans",Arial,sans-serif;color:var(--text);position:relative}
.abs{position:absolute}
.btn-dark{display:inline-block;background:var(--dark);color:var(--white);font:700 13px "Lato",sans-serif;letter-spacing:1px;padding:9px 20px;border-radius:4px;text-transform:uppercase}
.section-title{font:400 32px "Lato",sans-serif;letter-spacing:3px;text-transform:uppercase;color:var(--ink);text-align:center}
.title-rule{display:flex;justify-content:center;gap:8px;margin-top:16px}
.title-rule span{display:block;height:5px;width:56px;background:var(--blue)}
.title-rule span:nth-child(2){width:48px}

/* top bar */
.topbar{top:0;left:0;width:1200px;height:31px;background:var(--dark);color:var(--white);font-size:13px}
.topbar .mail{left:100px;top:6px;display:flex;gap:8px;align-items:center}
.topbar .phone{left:520px;top:6px;display:flex;gap:8px;align-items:center}
.topbar .quote{left:970px;top:3px;background:var(--red);padding:3px 16px;font-weight:600}

/* header */
.header{top:31px;left:0;width:1200px;height:94px;background:var(--blue)}
.brand{left:100px;top:31px;font:900 24px/32px "Lato",sans-serif;letter-spacing:1px;color:var(--white);white-space:nowrap}
.nav{left:436px;top:0;display:flex;height:94px}
.nav a{color:var(--white);text-decoration:none;font:700 14px "Lato",sans-serif;letter-spacing:1px;padding:0 14px;line-height:94px;white-space:nowrap}
.nav a.active{background:var(--blue-dark)}
.search{left:1076px;top:35px}

/* hero */
.hero{top:125px;left:0;width:1200px;height:600px;background:linear-gradient(120deg,#a6a29c 0%,#6f7a86 40%,#c6beb3 100%)}
.hero-copy{top:300px;left:0;width:1200px;text-align:center;color:var(--white);font:400 44px "Lato",sans-serif;line-height:48px;letter-spacing:1px}
.hero-copy b{font-weight:900}
.hero-cta{left:540px;background:rgba(30,30,30,.75);color:var(--white);font:700 15px "Lato",sans-serif;letter-spacing:1px;padding:8px 16px;border-radius:3px}
.dots{left:548px;display:flex;gap:10px}
.dots i{width:18px;height:18px;border-radius:50%;background:var(--white)}
.dots i:first-child{background:var(--blue)}
.callback{top:634px;left:347px;width:532px;height:196px;background:var(--grey-soft);border:8px solid #d6d6d6}
.callback .head{background:#dcdcdc;padding:14px 20px;font:400 13px Georgia,serif;color:#333}
.callback .fields{display:flex;gap:16px;padding:20px 20px 12px}
.callback .field{flex:1;height:36px;border:1px solid #bbb;background:#f9f9f9;font-size:13px;color:#888;padding:9px 12px}
.callback .row{padding:0 20px;display:flex;align-items:center;gap:10px}
.callback .send{background:var(--blue);color:var(--white);font:700 13px "Lato",sans-serif;padding:10px 16px}
.callback .apply{color:#f08a1c;font-size:13px}

/* equipment */
.equipment{top:870px;left:0;width:1200px}
.lead{width:996px;margin:40px auto 0;font-size:15px;line-height:26px;text-align:justify;letter-spacing:.5px}
.center{text-align:center;margin-top:36px}

/* services band */
.services{top:1205px;left:0;width:1200px;height:321px;background:var(--grey-band)}
.services .lower{position:absolute;left:0;top:180px;width:1200px;height:141px;background:#e5e5e5}
.cards{position:absolute;left:99px;top:21px;display:flex;gap:32px}
.card{width:226px;height:269px;background:var(--white);box-shadow:0 4px 10px rgba(0,0,0,.3);text-align:center;padding-top:18px}
.card .art{width:90px;height:90px;margin:0 auto;border-radius:8px}
.card h3{font:700 29px "Lato",sans-serif;color:var(--ink);margin-top:14px;letter-spacing:.5px}
.card p{font-size:12px;line-height:16px;text-align:left;padding:4px 24px;color:#555}
.card p.bold{font-weight:700;color:#222;font-size:13px}
.card .btn-dark{font-size:11px;padding:6px 14px;margin-top:8px}

/* reviews */
.reviews{top:1570px;left:0;width:1200px}
.review-row{display:flex;justify-content:center;gap:40px;margin-top:70px}
.review{width:300px;text-align:center}
.avatar{width:92px;height:92px;border-radius:50%;margin:0 auto;border:4px solid #e6e6e6}
.review .who{color:var(--blue);font-size:11px;letter-spacing:1px;text-transform:uppercase;margin-top:16px}
.review p{font-size:11px;line-height:15px;color:#555;margin-top:10px}
.review .more{color:var(--blue);font-size:11px}

/* business + key people */
.split{left:0;width:1200px;background:#ececec}
.photo{position:absolute;top:0;width:595px;height:100%}
.split .copy{position:absolute;width:470px;text-align:center}
.split .copy p{font-size:14.5px;line-height:23.5px;text-align:justify;margin-top:34px;letter-spacing:.4px}

/* partners */
.partners{top:2979px;left:0;width:1200px;height:308px;background:var(--blue);color:var(--white)}
.partners .intro{text-align:center;font-size:15px;padding-top:28px}
.logos{position:absolute;left:104px;top:68px;display:flex;gap:30px}
.logo-box{width:226px;height:162px;background:var(--white);display:flex;flex-direction:column;align-items:center;justify-content:center;gap:10px}
.logo-box .mark{width:44px;height:44px;border-radius:50%;background:var(--blue-dark)}
.logo-box .name{font:700 17px "Lato",sans-serif;color:#1d2b3a;text-transform:uppercase;letter-spacing:.5px}

/* message */
.message{top:3287px;left:0;width:1200px;height:352px;background:var(--grey-soft)}
.message h2{text-align:center;font:700 26px "Lato",sans-serif;letter-spacing:2px;color:var(--ink);padding-top:52px}
.form{position:absolute;left:120px;top:135px;display:grid;grid-template-columns:480px 468px;column-gap:12px}
.form .left{display:flex;flex-direction:column;gap:20px}
.input{height:44px;border:1px solid #999;background:var(--white);font-size:14px;color:#888;padding:11px 18px}
.textarea{height:106px;border:1px solid #999;background:var(--white);font-size:14px;color:#888;padding:11px 18px}
.submit{margin-top:20px;height:44px;background:var(--dark);color:var(--white);text-align:center;font:700 15px "Lato",sans-serif;letter-spacing:1px;line-height:44px}

/* contact */
.contact{top:3639px;left:0;width:1200px;height:188px;background:var(--white);display:flex;justify-content:center}
.contact .col{width:350px;text-align:center;padding-top:4px}
.contact .ic{width:54px;height:54px;margin:0 auto;display:block}
.contact h4{font:400 24px "Lato",sans-serif;letter-spacing:1px;color:#333;margin-top:14px;text-transform:uppercase}
.contact p{font-size:15px;line-height:21px;color:#555}

/* footer */
.footer{top:3827px;left:0;width:1200px;height:86px;background:var(--dark);color:var(--white);font-size:15px}
.footer .copy{left:100px;top:32px}
.footer .policy{left:956px;top:32px;font-weight:700;letter-spacing:1px}
</style>
</head>
<body>

<div class="abs topbar">
  <div class="abs mail">
    <svg width="16" height="12" viewBox="0 0 16 12"><rect x=".5" y=".5" width="15" height="11" fill="none" stroke="#fff"/><path d="M1 1l7 6 7-6" fill="none" stroke="#fff"/></svg>
    contact@delwynhart.com
  </div>
  <div class="abs phone">
    <svg width="14" height="14" viewBox="0 0 24 24"><path d="M6.6 10.8c1.4 2.8 3.8 5.1 6.6 6.6l2.2-2.2c.3-.3.7-.4 1-.2 1.1.4 2.300.6 3.600.6.6 0 1 .4 1 1V20c0 .6-.4 1-1 1C10.600 21 3 13.400 3 4c0-.6.4-1 1-1h3.500c.6 0 1 .4 1 1 0 1.300.2 2.500.6 3.600.1.3 0 .7-.2 1z" fill="#fff"/></svg>
    +1 555 014 7720
  </div>
  <div class="abs quote">Quick Quote</div>
</div>

<header class="abs header">
  <div class="abs brand">MARCUS DELWYN-HART</div>
  <nav class="abs nav">
    <a class="active">HOME</a><a>BUSINESS</a><a>KEY PEOPLE</a><a>PRODUCTS</a><a>INVESTORS</a><a>CONTACT</a>
  </nav>
  <svg class="abs search" width="24" height="24" viewBox="0 0 24 24"><circle cx="10" cy="10" r="7" fill="none" stroke="#fff" stroke-width="3"/><path d="M15 15l7 7" stroke="#fff" stroke-width="3"/></svg>
</header>

<section class="abs hero" role="img" aria-label="Photo of smiling business colleagues gathered around a laptop in an office"></section>
<div class="abs hero-copy">BUYING OR REFINANCING?<br>COMPARE <b>HOME LOAN RATES</b></div>
<div class="abs hero-cta" style="top:535px">ENQUIRE NOW</div>
<div class="abs dots" style="top:580px"><i></i><i></i><i></i><i></i></div>
<svg class="abs" style="left:30px;top:357px" width="62" height="62" viewBox="0 0 62 62"><circle cx="31" cy="31" r="28" fill="none" stroke="#fff" stroke-width="4"/><path d="M36 18L22 31l14 13" fill="none" stroke="#fff" stroke-width="6"/></svg>
<svg class="abs" style="left:1108px;top:357px" width="62" height="62" viewBox="0 0 62 62"><circle cx="31" cy="31" r="28" fill="none" stroke="#fff" stroke-width="4"/><path d="M26 18l14 13-14 13" fill="none" stroke="#fff" stroke-width="6"/></svg>

<div class="abs callback">
  <div class="head">Get Funded Today, enter details below for a call back</div>
  <div class="fields"><div class="field">Phone Number</div><div class="field">Email Address</div></div>
  <div class="row"><span class="send">Get A Call Back</span><span class="apply">[Apply online]</span></div>
</div>

<section class="abs equipment">
  <h2 class="section-title">Equipment Finance</h2>
  <div class="title-rule"><span></span><span></span><span></span></div>
  <p class="lead">Lorem Ipsum is simply dummy text of the printing and typesetting industry. Lorem Ipsum has been the industry's standard dummy text ever since the 1500s, when an unknown printer took a galley of type and scrambled it to make a type specimen book. It has survived not only five centuries, but also the leap into electronic typesetting, remaining essentially unchanged It was popularised in the 1960s with the release of Letraset sheets containing Lorem Ipsum passages, and more recently with desktop publishing software like Aldus PageMaker including versions of Lorem Ipsum</p>
  <div class="center"><span class="btn-dark">Read More</span></div>
</section>

<section class="abs services">
  <div class="lower"></div>
  <div class="cards">
    <div class="card"><div class="art" role="img" aria-label="Illustration of a megaphone" style="background:#4a6fa5"></div><h3>Marketing</h3><p class="bold">Lorem Ipsum is simply</p><p>Lorem ipsum dolor sit amet, consectetur..</p><span class="btn-dark">Read More</span></div>
    <div class="card"><div class="art" role="img" aria-label="Illustration of a tree under a magnifier" style="background:#8cc152"></div><h3>Structure</h3><p class="bold">Lorem Ipsum is simply</p><p>Lorem ipsum dolor sit amet, consectetur..</p><span class="btn-dark">Read More</span></div>
    <div class="card"><div class="art" role="img" aria-label="Illustration of a house" style="background:#d9a441"></div><h3>Banking</h3><p class="bold">Lorem Ipsum is simply</p><p>Lorem ipsum dolor sit amet, consectetur..</p><span class="btn-dark">Read More</span></div>
    <div class="card"><div class="art" role="img" aria-label="Illustration of a clock with tools" style="background:#e0773a"></div><h3>Consulting</h3><p class="bold">Lorem Ipsum is simply</p><p>Lorem ipsum dolor sit amet, consectetur..</p><span class="btn-dark">Read More</span></div>
  </div>
</section>
<svg class="abs" style="left:22px;top:1336px" width="44" height="44" viewBox="0 0 44 44"><circle cx="22" cy="22" r="21" fill="#8a8a8a"/><path d="M25 13l-9 9 9 9" fill="none" stroke="#fff" stroke-width="4"/></svg>
<svg class="abs" style="left:1126px;top:1336px" width="44" height="44" viewBox="0 0 44 44"><circle cx="22" cy="22" r="21" fill="#8a8a8a"/><path d="M19 13l9 9-9 9" fill="none" stroke="#fff" stroke-width="4"/></svg>

<section class="abs reviews">
  <h2 class="section-title">See Some of the Reviews Here</h2>
  <div class="title-rule"><span></span><span></span><span></span></div>
  <div class="review-row">
    <div class="review"><div class="avatar" role="img" aria-label="Portrait of client" style="background:#b08a70"></div><div class="who">Dana Orlov, Brightfold Studio</div><p>"They found us sound finance fast. That meant better cash flow and lower repayments, keeping our fleet running all year."</p><span class="more">Read their story »</span></div>
    <div class="review"><div class="avatar" role="img" aria-label="Portrait of client" style="background:#9c8a7e"></div><div class="who">Owen Farrant, Kestrel Digital</div><p>"Our loan was settled in days. Clear advice, honest rates and a team that explained every step of the process to us."</p><span class="more">Read their story »</span></div>
    <div class="review"><div class="avatar" role="img" aria-label="Portrait of client" style="background:#a58670"></div><div class="who">Lena Marsh, Corvale Partners</div><p>"The choice to work with them was a smart move. We now have the funds we need and the confidence to grow."</p><span class="more">Read their story »</span></div>
  </div>
</section>

<section class="abs split" style="top:2035px;height:470px">
  <div class="photo" style="left:0;background:linear-gradient(135deg,#8fa0b0,#cfc7bd)" role="img" aria-label="Photo of business team meeting around a table"></div>
  <div class="copy" style="left:665px;top:50px">
    <h2 class="section-title">The Business</h2>
    <div class="title-rule"><span></span><span></span><span></span></div>
    <p>Lorem Ipsum is simply dummy text of the printing and typesetting industry. Lorem Ipsum has been the industry's standard dummy text ever since the 1500s, when an unknown printer took a galley of type and scrambled it to make a type specimen book. It has survived not only five centuries, but also the leap into electronic typesetting, remaining essentially unchanged It was popularised in the 1960s with the release of Letraset sheets contain Lorem Ipsum passages, and more recently with desktop publishing software.</p>
    <div style="margin-top:26px"><span class="btn-dark">Read More</span></div>
  </div>
</section>

<section class="abs split" style="top:2505px;height:474px">
  <div class="photo" style="left:597px;width:603px;background:linear-gradient(135deg,#c9c2b6,#7f8d9c)" role="img" aria-label="Photo of colleagues discussing documents at a meeting table"></div>
  <div class="copy" style="left:68px;top:50px">
    <h2 class="section-title">Key People</h2>
    <div class="title-rule"><span></span><span></span><span></span></div>
    <p>Lorem Ipsum is simply dummy text of the printing and typesetting industry. Lorem Ipsum has been the industry's standard dummy text ever since the 1500s, when an un known printer took a galley of type and scrambled it to make a type specimen book. It has survived not only five centuries, but also the leap into electronic typesetting, remaining essentially unchanged it was popularised in the 1960s with the release of Letraset sheets contain Lorem Ipsum passages, and more recently with desktop publishing software.</p>
    <div style="margin-top:26px"><span class="btn-dark">Read More</span></div>
  </div>
</section>

<section class="abs partners">
  <p class="intro">We compare loan and insurance products from some of Australia's leading finance and insurance companies.</p>
  <div class="logos">
    <div class="logo-box"><div class="mark"></div><div class="name">Ledgerpost</div></div>
    <div class="logo-box"><div class="mark"></div><div class="name">Numerval</div></div>
    <div class="logo-box"><div class="mark"></div><div class="name">Harrow &amp; Quill CPA</div></div>
    <div class="logo-box"><div class="mark"></div><div class="name">Company Name</div></div>
  </div>
  <svg class="abs" style="left:30px;top:122px" width="50" height="50" viewBox="0 0 50 50"><circle cx="25" cy="25" r="23" fill="none" stroke="#fff" stroke-width="3"/><path d="M29 15l-10 10 10 10" fill="none" stroke="#fff" stroke-width="5"/></svg>
  <svg class="abs" style="left:1120px;top:122px" width="50" height="50" viewBox="0 0 50 50"><circle cx="25" cy="25" r="23" fill="none" stroke="#fff" stroke-width="3"/><path d="M21 15l10 10-10 10" fill="none" stroke="#fff" stroke-width="5"/></svg>
</section>

<section class="abs message">
  <h2>SEND A MESSAGE</h2>
  <div class="form">
    <div class="left">
      <div class="input">Your Name</div>
      <div class="input">Your Email</div>
      <div class="input">Subject</div>
    </div>
    <div>
      <div class="textarea">Your Message</div>
      <div class="submit">SUBMIT</div>
    </div>
  </div>
</section>

<section class="abs contact">
  <div class="col">
    <svg class="ic" viewBox="0 0 54 54"><circle cx="27" cy="27" r="25" fill="none" stroke="#1c9ad6" stroke-width="3"/><path d="M15 28l12-11 12 11M19 25v12h6v-7h4v7h6V25" fill="none" stroke="#1c9ad6" stroke-width="3"/></svg>
    <h4>Our Adress</h4>
    <p>4821 Harlow Street,<br>Suite 721</p>
  </div>
  <div class="col">
    <svg class="ic" viewBox="0 0 54 54"><circle cx="27" cy="27" r="25" fill="none" stroke="#1c9ad6" stroke-width="3"/><rect x="15" y="19" width="24" height="16" fill="none" stroke="#1c9ad6" stroke-width="3"/><path d="M15 19l12 10 12-10" fill="none" stroke="#1c9ad6" stroke-width="3"/></svg>
    <h4>Our Email</h4>
    <p>email@yourdomain.com</p>
  </div>
  <div class="col">
    <svg class="ic" viewBox="0 0 54 54"><circle cx="27" cy="27" r="25" fill="none" stroke="#1c9ad6" stroke-width="3"/><path d="M20 16c-2 0-4 2-3 5 2 7 8 13 15 15 3 1 5-1 5-3l-4-4-3 2c-3-1-6-4-7-7l2-3z" fill="#1c9ad6"/></svg>
    <h4>Call Us</h4>
    <p>+1 (0) 101 0000 000</p>
  </div>
</section>

<footer class="abs footer">
  <div class="abs copy">Copyright © 2017 <b>Marcus Delwyn-Hart</b>. All Rights Reserved.</div>
  <div class="abs policy">PRIVACY &amp; POLICY</div>
</footer>

</body>
</html>
```